PowerPoint Template - Swiss Tech Venture Fund

We are creating a fund to invest in swiss tech startups. We are entrepreneurs and we are building a model where we will not only invest in the startups but also help them scale.

We need ASAP a powerpoint template design to start our work. In couple of months, we will also need a proper website (as the one we have today, dalq7.ch) is not branded enough and too lightweight in terms of content.

For the ppt, we need
A PowerPoint master template
Fully editable slides
Consistent typography, layout, and visual system

Regarding the design, couple of hints
- We are swiss-based so we have to “feel it” in the presentation (symbols, mountains, etc).
- We are focused on Trust and Security technology. So it needs to be reflected as well (icons, typo, etc)
- The design should be primarily aligned with our new logo (see attached). We have a temporary website, but it should not be treated as a final reference (dalq7.ch)
- The design needs to feel “professional” as we are talking to institutions but also being able to be present to innovative tech startups
- We like very much the work done for another company (https://www.pixelvantora.com/design/58190276). So maybe a modified version of this one.

Target Market(s)

Institutional investors

Industry/Entity Type

Investment

Other font styles liked:
• Light compatible with the logo

Requirements
Must have
• Pictures (and not cartoon-like design). Icons that match our brand (trust and security)

```html
<!DOCTYPE html>
<html lang="en">
<head>
<meta charset="utf-8">
<title>DALQ7 – Presentation Template</title>
<link href="https://fonts.googleapis.com/css2?family=Poppins:wght@300;400;500;600;700&display=swap" rel="stylesheet">
<style>
  :root{
    --bg:#d3d4cc;
    --paper:#ffffff;
    --red:#e30613;
    --red-deep:#c70510;
    --ink:#111111;
    --char:#3a3a3a;
    --grey:#b3b3b3;
    --track:#eeeeee;
    --muted:#8a8a8a;
    --faint:#bdbdbd;
  }
  *{margin:0;padding:0;box-sizing:border-box}
  html,body{width:901px;height:1200px;overflow:hidden;background:var(--bg)}
  body{position:relative;font-family:'Poppins',sans-serif}
  .slide{position:absolute;width:368px;height:206px;background:var(--paper);box-shadow:0 6px 14px rgba(0,0,0,.18);overflow:hidden}
  .slide svg{display:block;width:100%;height:100%}
  .icon-sprites{position:absolute;width:0;height:0;overflow:hidden}
  text{font-family:'Poppins',sans-serif}
  .logo{font-size:15px;font-weight:600;fill:var(--ink);letter-spacing:.5px}
  .title{font-size:34px;font-weight:400;fill:var(--ink)}
  .title .accent{fill:var(--red)}
  .h2{font-size:27px;font-weight:400;fill:var(--ink)}
  .kicker{font-size:8px;font-weight:600;fill:var(--ink)}
  .kicker-wide{font-size:9px;font-weight:500;fill:var(--ink);letter-spacing:2.5px}
  .label{font-size:8px;font-weight:600;fill:var(--char);letter-spacing:1.5px}
  .label-sm{font-size:7px;font-weight:700;fill:var(--ink);letter-spacing:.6px}
  .body{font-size:5.6px;font-weight:400;fill:var(--muted)}
  .body-dark{font-size:5.6px;font-weight:400;fill:var(--char)}
  .pct{font-size:9px;font-weight:500;fill:var(--char);letter-spacing:1.5px}
  .stat{font-size:15px;font-weight:600;fill:var(--ink)}
  .stat-sm{font-size:5px;fill:var(--muted)}
  .axis{font-size:6px;fill:var(--muted)}
  .footer-url{font-size:8px;fill:var(--char)}
  .pager{font-size:6.5px;fill:var(--faint)}
  .num{font-size:10px;font-weight:500;fill:var(--ink)}
  .num-sm{font-size:6px;font-weight:600;fill:#fff}
  .white{fill:#fff}
</style>
</head>
<body>

<svg class="icon-sprites" aria-hidden="true">
  <symbol id="ic-shield" viewBox="0 0 24 24"><path fill="currentColor" d="M12 2l8 3v6c0 5-3.5 9-8 11-4.5-2-8-6-8-11V5z"/></symbol>
  <symbol id="ic-camera" viewBox="0 0 24 24"><path fill="currentColor" fill-rule="evenodd" d="M8 5l1.5-2h5L16 5h4a2 2 0 0 1 2 2v11a2 2 0 0 1-2 2H4a2 2 0 0 1-2-2V7a2 2 0 0 1 2-2zM7.5 12.5a4.5 4.5 0 1 0 9 0a4.5 4.5 0 1 0-9 0z"/><circle cx="12" cy="12.5" r="2.6" fill="currentColor"/></symbol>
  <symbol id="ic-trophy" viewBox="0 0 24 24"><path fill="currentColor" d="M6 3h12v3h3v3a4 4 0 0 1-4 4h-.5A5 5 0 0 1 13 15.9V18h3v3H8v-3h3v-2.1A5 5 0 0 1 7.5 13H7a4 4 0 0 1-4-4V6h3zM5 8v1a2 2 0 0 0 2 2V8zm14 0h-2v3a2 2 0 0 0 2-2z"/></symbol>
  <symbol id="ic-rocket" viewBox="0 0 24 24"><path fill="currentColor" d="M20 4c-5 0-9 3-11 8l3 3c5-2 8-6 8-11zM8 13l-4 1 2-4h3zM11 16l-1 4 4-2v-3zM6 16c-2 1-2 3-2 4 1 0 3 0 4-2z"/></symbol>
  <symbol id="ic-cloud" viewBox="0 0 24 24"><path fill="currentColor" d="M7 18a5 5 0 0 1-.5-10A6 6 0 0 1 18 9a4.5 4.5 0 0 1 0 9z"/></symbol>
  <symbol id="ic-puzzle" viewBox="0 0 24 24"><path fill="currentColor" d="M4 8h4a2 2 0 1 1 4 0h4v4a2 2 0 1 1 0 4v4h-4a2 2 0 1 0-4 0H4v-4a2 2 0 1 0 0-4z"/></symbol>
  <marker id="arrow-red" viewBox="0 0 10 10" refX="5" refY="5" markerWidth="5" markerHeight="5" orient="auto-start-reverse"><path d="M0 0L10 5L0 10z" fill="#e30613"/></marker>
  <marker id="arrow-ink" viewBox="0 0 10 10" refX="5" refY="5" markerWidth="5" markerHeight="5" orient="auto-start-reverse"><path d="M0 0L10 5L0 10z" fill="#111"/></marker>
  <marker id="arrow-white" viewBox="0 0 10 10" refX="5" refY="5" markerWidth="4" markerHeight="4" orient="auto-start-reverse"><path d="M0 0L10 5L0 10z" fill="#fff"/></marker>
</svg>

<!-- Data Chart -->
<section class="slide" style="left:87px;top:64px">
  <svg viewBox="0 0 680 380">
    <text class="title" x="62" y="80">Data <tspan class="accent">Chart</tspan></text>
    <text class="logo" x="602" y="42">DALQ7</text>
    <g fill="none" stroke-width="8">
      <g transform="rotate(-90 118 189)"><circle cx="118" cy="189" r="50" stroke="var(--track)"/><circle cx="118" cy="189" r="50" stroke="var(--char)" stroke-dasharray="204.2 400"/></g>
      <g transform="rotate(-90 267 189)"><circle cx="267" cy="189" r="50" stroke="var(--track)"/><circle cx="267" cy="189" r="50" stroke="var(--red)" stroke-dasharray="141.4 400"/></g>
      <g transform="rotate(-90 415 189)"><circle cx="415" cy="189" r="50" stroke="var(--track)"/><circle cx="415" cy="189" r="50" stroke="var(--char)" stroke-dasharray="157 400"/></g>
      <g transform="rotate(-90 560 189)"><circle cx="560" cy="189" r="50" stroke="var(--track)"/><circle cx="560" cy="189" r="50" stroke="var(--red)" stroke-dasharray="295.3 400"/></g>
    </g>
    <g text-anchor="middle">
      <text class="pct" x="118" y="197">65%</text><text class="pct" x="267" y="197">45%</text>
      <text class="pct" x="415" y="197">50%</text><text class="pct" x="560" y="197">94%</text>
      <text class="label" x="118" y="281">TITLE</text><text class="label" x="267" y="281">TITLE</text>
      <text class="label" x="415" y="281">TITLE</text><text class="label" x="560" y="281">TITLE</text>
      <g class="body">
        <text x="118" y="298">A peep at some distant orb has power to</text><text x="118" y="310">raise and purify our thoughts like a music</text>
        <text x="267" y="298">A peep at some distant orb has power to</text><text x="267" y="310">raise and purify our thoughts like a music</text>
        <text x="415" y="298">A peep at some distant orb has power to</text><text x="415" y="310">raise and purify our thoughts like a music</text>
        <text x="560" y="298">A peep at some distant orb has power to</text><text x="560" y="310">raise and purify our thoughts like a music</text>
      </g>
    </g>
    <text class="footer-url" x="33" y="355">www. dalq7.ch</text>
    <text class="pager" x="588" y="349">01 /&#160;&#160;39</text><text class="pager" x="588" y="364">Welcome Slide</text>
  </svg>
</section>

<!-- Financials Facts -->
<section class="slide" style="left:465px;top:64px">
  <svg viewBox="0 0 680 380">
    <text class="title" x="62" y="80">Financials <tspan class="accent">Facts</tspan></text>
    <text class="logo" x="602" y="42">DALQ7</text>
    <g stroke="#e6e6e6" stroke-width="1">
      <line x1="93" y1="130" x2="93" y2="315"/><line x1="138" y1="130" x2="138" y2="315"/><line x1="183" y1="130" x2="183" y2="315"/>
      <line x1="228" y1="130" x2="228" y2="315"/><line x1="273" y1="130" x2="273" y2="315"/><line x1="318" y1="130" x2="318" y2="315"/><line x1="363" y1="130" x2="363" y2="315"/>
    </g>
    <g>
      <rect x="93" y="140" width="225" height="8" fill="var(--char)"/><rect x="93" y="149" width="126" height="8" fill="var(--red)"/><rect x="93" y="158" width="202" height="8" fill="var(--grey)"/>
      <rect x="93" y="185" width="135" height="8" fill="var(--char)"/><rect x="93" y="194" width="81" height="8" fill="var(--red)"/><rect x="93" y="203" width="157" height="8" fill="var(--grey)"/>
      <rect x="93" y="231" width="90" height="8" fill="var(--char)"/><rect x="93" y="240" width="198" height="8" fill="var(--red)"/><rect x="93" y="249" width="112" height="8" fill="var(--grey)"/>
      <rect x="93" y="276" width="90" height="8" fill="var(--char)"/><rect x="93" y="285" width="108" height="8" fill="var(--red)"/><rect x="93" y="294" width="193" height="8" fill="var(--grey)"/>
    </g>
    <g class="axis" text-anchor="end">
      <text x="86" y="156">Category 4</text><text x="86" y="201">Category 3</text><text x="86" y="247">Category 2</text><text x="86" y="292">Category 1</text>
    </g>
    <g class="axis" text-anchor="middle">
      <text x="93" y="325">0</text><text x="138" y="325">1</text><text x="183" y="325">2</text><text x="228" y="325">3</text><text x="273" y="325">4</text><text x="318" y="325">5</text><text x="363" y="325">6</text>
    </g>
    <g class="axis">
      <rect x="164" y="335" width="4" height="4" fill="var(--char)"/><text x="170" y="339">Series 3</text>
      <rect x="199" y="335" width="4" height="4" fill="var(--red)"/><text x="205" y="339">Series 2</text>
      <rect x="234" y="335" width="4" height="4" fill="var(--grey)"/><text x="240" y="339">Series 1</text>
    </g>
    <g text-anchor="middle">
      <text class="stat" x="435" y="145">18.5K</text><text class="stat-sm" x="435" y="160">Sessions</text>
      <text class="stat" x="567" y="145">980.5K</text><text class="stat-sm" x="567" y="160">View</text>
      <text class="stat" x="435" y="228">2.8M</text><text class="stat-sm" x="435" y="243">Visit</text>
      <rect x="508" y="194" width="114" height="62" fill="var(--char)" style="filter:drop-shadow(0 3px 4px rgba(0,0,0,.3))"/>
      <text class="stat white" x="567" y="228">$10.4M</text><text class="stat-sm" x="567" y="243" style="fill:#cfcfcf">Sales</text>
      <text class="stat" x="435" y="308">15:50</text><text class="stat-sm" x="435" y="323">Duration</text>
      <text class="stat" x="567" y="308">40%</text><text class="stat-sm" x="567" y="323">Rate</text>
    </g>
    <text class="footer-url" x="33" y="355">www. dalq7.ch</text>
    <text class="pager" x="588" y="349">01 /&#160;&#160;39</text><text class="pager" x="588" y="364">Welcome Slide</text>
  </svg>
</section>

<!-- Infographic: business system petals -->
<section class="slide" style="left:87px;top:280px">
  <svg viewBox="0 0 680 380">
    <text class="kicker" x="340" y="46" text-anchor="middle">Business System</text>
    <text class="h2" x="340" y="73" text-anchor="middle">Infographic</text>
    <text class="logo" x="602" y="42">DALQ7</text>
    <path d="M226 152a52 52 0 0 1 52-52h0a52 52 0 0 1 52 52v51h-52a52 52 0 0 1-52-52z" fill="var(--ink)"/>
    <path d="M342 152a52 52 0 0 1 52-52a52 52 0 0 1 52 52a52 52 0 0 1-52 51h-52z" fill="var(--red)"/>
    <path d="M226 267a52 52 0 0 1 52-52h52v51a52 52 0 0 1-52 52a52 52 0 0 1-52-51z" fill="var(--red)"/>
    <path d="M344 215h52a52 52 0 0 1 52 52a52 52 0 0 1-52 51a52 52 0 0 1-52-51z" fill="var(--ink)"/>
    <use href="#ic-shield" x="264" y="134" width="30" height="30" color="#fff"/>
    <use href="#ic-camera" x="379" y="134" width="30" height="30" color="#fff"/>
    <use href="#ic-trophy" x="263" y="249" width="30" height="30" color="#fff"/>
    <use href="#ic-rocket" x="381" y="249" width="30" height="30" color="#fff"/>
    <g text-anchor="end">
      <text class="label-sm" x="199" y="135">TEXT TITTLE</text><text class="label-sm" x="199" y="144">HERE</text>
      <text class="body" x="199" y="157">Lorem ipsum dolor siabes dolore magna</text><text class="body" x="199" y="167">aliqua utaners enim vas adtera intesilar</text><text class="body" x="199" y="177">lasiedonisi aliquie com.</text>
      <text class="label-sm" x="199" y="257">TEXT TITTLE</text><text class="label-sm" x="199" y="266">HERE</text>
      <text class="body" x="199" y="279">Lorem ipsum dolor siabes dolore magna</text><text class="body" x="199" y="289">aliqua utaners enim vas adtera intesilar</text><text class="body" x="199" y="299">lasiedonisi aliquie com.</text>
    </g>
    <text class="label-sm" x="473" y="135">TEXT TITTLE</text><text class="label-sm" x="473" y="144">HERE</text>
    <text class="body" x="473" y="157">Lorem ipsum dolor siabes dolore magna</text><text class="body" x="473" y="167">aliqua utaners enim vas adtera intesilar</text><text class="body" x="473" y="177">lasiedonisi aliquie com.</text>
    <text class="label-sm" x="473" y="257">TEXT TITTLE</text><text class="label-sm" x="473" y="266">HERE</text>
    <text class="body" x="473" y="279">Lorem ipsum dolor siabes dolore magna</text><text class="body" x="473" y="289">aliqua utaners enim vas adtera intesilar</text><text class="body" x="473" y="299">lasiedonisi aliquie com.</text>
    <text class="footer-url" x="33" y="355">www. dalq7.ch</text>
    <text class="pager" x="588" y="349">01 /&#160;&#160;39</text><text class="pager" x="588" y="364">Welcome Slide</text>
  </svg>
</section>

<!-- Infographic: business model ring -->
<section class="slide" style="left:465px;top:280px">
  <svg viewBox="0 0 680 380">
    <text class="kicker" x="339" y="46" text-anchor="middle">Business Model</text>
    <text class="h2" x="339" y="72" text-anchor="middle">Infographic</text>
    <text class="logo" x="602" y="42">DALQ7</text>
    <path d="M231 209A108 108 0 0 1 339 101L339 154A55 55 0 0 0 284 209Z" fill="var(--ink)"/>
    <path d="M339 101A108 108 0 0 1 447 209L394 209A55 55 0 0 0 339 154Z" fill="var(--red)"/>
    <path d="M447 209A108 108 0 0 1 339 317L339 264A55 55 0 0 0 394 209Z" fill="var(--ink)"/>
    <path d="M339 317A108 108 0 0 1 231 209L284 209A55 55 0 0 0 339 264Z" fill="var(--red)"/>
    <g stroke="#fff" stroke-width="5"><line x1="339" y1="98" x2="339" y2="320"/><line x1="228" y1="209" x2="450" y2="209"/></g>
    <circle cx="339" cy="209" r="52" fill="#fff"/>
    <text x="339" y="218" text-anchor="middle" style="font-size:23px;font-weight:600;fill:var(--char)">DALQ7</text>
    <g style="filter:drop-shadow(0 2px 3px rgba(0,0,0,.3))">
      <circle cx="259" cy="137" r="32" fill="var(--red)"/><circle cx="420" cy="142" r="32" fill="var(--ink)"/>
      <circle cx="262" cy="280" r="32" fill="var(--ink)"/><circle cx="415" cy="284" r="32" fill="var(--red)"/>
    </g>
    <use href="#ic-shield" x="245" y="123" width="28" height="28" color="#fff"/>
    <use href="#ic-camera" x="406" y="128" width="28" height="28" color="#fff"/>
    <use href="#ic-trophy" x="248" y="266" width="28" height="28" color="#fff"/>
    <use href="#ic-rocket" x="401" y="270" width="28" height="28" color="#fff"/>
    <g text-anchor="end">
      <text class="label-sm" x="199" y="125">TEXT TITTLE</text><text class="label-sm" x="199" y="134">HERE</text>
      <text class="body" x="199" y="144">Lorem ipsum dolor siabes dolore magna</text><text class="body" x="199" y="156">aliqua utaners enim vas adtera intesilar</text><text class="body" x="199" y="168">lasiedonisi aliquie com.</text>
      <text class="label-sm" x="199" y="260">TEXT TITTLE</text><text class="label-sm" x="199" y="269">HERE</text>
      <text class="body" x="199" y="279">Lorem ipsum dolor siabes dolore magna</text><text class="body" x="199" y="291">aliqua utaners enim vas adtera intesilar</text><text class="body" x="199" y="303">lasiedonisi aliquie com.</text>
    </g>
    <text class="label-sm" x="472" y="125">TEXT TITTLE</text><text class="label-sm" x="472" y="134">HERE</text>
    <text class="body" x="472" y="144">Lorem ipsum dolor siabes dolore magna</text><text class="body" x="472" y="156">aliqua utaners enim vas adtera intesilar</text><text class="body" x="472" y="168">lasiedonisi aliquie com.</text>
    <text class="label-sm" x="472" y="265">TEXT TITTLE</text><text class="label-sm" x="472" y="274">HERE</text>
    <text class="body" x="472" y="284">Lorem ipsum dolor siabes dolore magna</text><text class="body" x="472" y="296">aliqua utaners enim vas adtera intesilar</text><text class="body" x="472" y="308">lasiedonisi aliquie com.</text>
    <text class="footer-url" x="33" y="355">www. dalq7.ch</text>
    <text class="pager" x="588" y="349">01 /&#160;&#160;39</text><text class="pager" x="588" y="364">Welcome Slide</text>
  </svg>
</section>

<!-- Infographic: business idea arcs -->
<section class="slide" style="left:87px;top:496px">
  <svg viewBox="0 0 680 380">
    <text class="logo" x="602" y="42">DALQ7</text>
    <path d="M0 380A225 225 0 0 1 450 380Z" fill="var(--ink)"/>
    <path d="M225 380L-3 380A228 228 0 0 1 111 183Z" fill="var(--red)"/>
    <path d="M225 380L65 380A160 160 0 0 1 317 249Z" fill="var(--red-deep)"/>
    <path d="M130 380A95 95 0 0 1 320 380Z" fill="var(--red)"/>
    <path d="M197 380A28 28 0 0 1 253 380Z" fill="var(--ink)"/>
    <g stroke="var(--red)" stroke-width="3" fill="none">
      <line x1="125" y1="215" x2="86" y2="137" marker-end="url(#arrow-red)"/>
      <line x1="280" y1="255" x2="332" y2="164" marker-end="url(#arrow-red)"/>
      <line x1="330" y1="374" x2="412" y2="374" marker-end="url(#arrow-red)"/>
    </g>
    <use href="#ic-cloud" x="94" y="214" width="28" height="28" color="#fff"/>
    <use href="#ic-puzzle" x="234" y="245" width="24" height="24" color="#fff"/>
    <use href="#ic-rocket" x="270" y="340" width="24" height="24" color="#fff"/>
    <g class="kicker" style="font-size:6px">
      <text x="113" y="44">Lorem ipsum</text><text x="113" y="51">Dolor</text><text x="113" y="58">Sit amet.</text>
      <text x="276" y="40">Lorem ipsum</text><text x="276" y="47">Dolor</text><text x="276" y="54">Sit amet.</text>
      <text x="492" y="241">Lorem ipsum</text><text x="492" y="248">Dolor</text><text x="492" y="255">Sit amet.</text>
    </g>
    <g stroke="#999" stroke-width=".8"><line x1="113" y1="76" x2="222" y2="76"/><line x1="276" y1="72" x2="385" y2="72"/><line x1="492" y1="274" x2="598" y2="274"/></g>
    <g class="body-dark" style="font-size:4.6px">
      <text x="113" y="97">Lorep ipsum duis aute irure dolor in kaseih</text><text x="113" y="105">oilue reprehendesse cili inure dolorioru sit</text><text x="113" y="113">amet. Duis aute iruslakus reprei Voluptate</text><text x="113" y="121">lorem kuisais.</text>
      <text x="276" y="93">Lorep ipsum duis aute irure dolor in kaseih</text><text x="276" y="101">oilue reprehendesse cili inure dolorioru sit</text><text x="276" y="109">amet. Duis aute iruslakus reprei Voluptate</text><text x="276" y="117">lorem kuisais.</text>
      <text x="492" y="294">Lorep ipsum duis aute irure dolor in kaseih</text><text x="492" y="302">oilue reprehendesse cili inure dolorioru sit</text><text x="492" y="310">amet. Duis aute iruslakus reprei Voluptate</text><text x="492" y="318">lorem kuisais.</text>
    </g>
    <text class="kicker-wide" x="438" y="69">BUSINESS IDEA</text>
    <text class="h2" x="438" y="97">Infographic</text>
    <g class="body-dark" style="font-size:5px">
      <text x="440" y="133">Lorep ipsum duis aute irure dolor in kausel oilue</text><text x="440" y="142">eprehe deriti volis esse cili inure dolori laboru sit amet</text><text x="440" y="151">Duis autelo iruslakus repre hendari Voluptate lorem</text><text x="440" y="160">kuisais.</text>
      <text x="440" y="186">Lorep ipsum duis aute irure dolor in kausel oilue</text><text x="440" y="195">eprehe deriti volis esse cili inure dolori laboru sit amet</text><text x="440" y="204">Duis autelo iruslakus repre hendari Voluptate lorem</text><text x="440" y="213">kuisais. Sit ametol</text>
    </g>
    <text class="pager" x="588" y="349">01 /&#160;&#160;39</text><text class="pager" x="588" y="364">Welcome Slide</text>
  </svg>
</section>

<!-- Infographic: process loop -->
<section class="slide" style="left:465px;top:496px">
  <svg viewBox="0 0 680 380">
    <text x="335" y="48" text-anchor="middle" style="font-size:9px;font-weight:500;fill:var(--ink)">Business <tspan font-weight="700">System</tspan></text>
    <text class="h2" x="342" y="82" text-anchor="middle">Infographic</text>
    <text class="logo" x="602" y="42">DALQ7</text>
    <rect x="145" y="200" width="405" height="128" rx="64" fill="none" stroke="#d0d0d0" stroke-width="2.5"/>
    <path d="M145 264A64 64 0 0 0 209 328H340" fill="none" stroke="var(--ink)" stroke-width="2.5"/>
    <path d="M340 328H486A64 64 0 0 0 550 264" fill="none" stroke="var(--red)" stroke-width="2.5"/>
    <path d="M144 264l-4 8h8z" fill="var(--ink)"/><path d="M549 264l-4 8h8z" fill="var(--red)" transform="rotate(180 549 268)"/>
    <path d="M230 328l8-4v8z" fill="var(--red)"/><path d="M335 328l8-4v8z" fill="var(--ink)"/><path d="M450 328l8-4v8z" fill="var(--red)"/>
    <polygon points="500,242 512,242 532,263 512,284 500,284 520,263" fill="#cfcfcf"/>
    <polygon points="420,242 480,242 500,263 480,284 420,284 440,263" fill="var(--ink)"/>
    <polygon points="345,242 400,242 420,263 400,284 345,284 365,263" fill="var(--red)"/>
    <polygon points="265,242 325,242 345,263 325,284 265,284 285,263" fill="var(--ink)"/>
    <polygon points="189,242 245,242 265,263 245,284 189,284" fill="var(--red)"/>
    <use href="#ic-puzzle" x="219" y="254" width="18" height="18" color="#fff"/>
    <use href="#ic-rocket" x="297" y="254" width="18" height="18" color="#fff"/>
    <use href="#ic-shield" x="372" y="254" width="18" height="18" color="#fff"/>
    <use href="#ic-cloud" x="448" y="252" width="22" height="22" color="#fff"/>
    <rect x="295" y="114" width="88" height="40" rx="3" fill="var(--ink)"/>
    <use href="#ic-trophy" x="329" y="124" width="20" height="20" color="#fff"/>
    <g fill="none" stroke="var(--char)" stroke-width="1" stroke-dasharray="2 2">
      <path d="M228 184Q236 138 289 134" marker-end="url(#arrow-ink)"/>
      <path d="M448 184Q440 138 389 134" marker-end="url(#arrow-ink)"/>
      <path d="M302 184L318 160" marker-end="url(#arrow-ink)"/>
      <path d="M376 184L360 160" marker-end="url(#arrow-ink)"/>
    </g>
    <g stroke-width="1.5">
      <line x1="228" y1="238" x2="228" y2="218" stroke="var(--ink)" marker-end="url(#arrow-ink)"/>
      <line x1="302" y1="238" x2="302" y2="218" stroke="var(--red)" marker-end="url(#arrow-red)"/>
      <line x1="376" y1="238" x2="376" y2="218" stroke="var(--ink)" marker-end="url(#arrow-ink)"/>
      <line x1="448" y1="238" x2="448" y2="218" stroke="var(--red)" marker-end="url(#arrow-red)"/>
    </g>
    <g fill="#fff" stroke-width="2.5">
      <circle cx="228" cy="200" r="14" stroke="var(--ink)"/><circle cx="302" cy="200" r="14" stroke="var(--red)"/>
      <circle cx="376" cy="200" r="14" stroke="var(--ink)"/><circle cx="448" cy="200" r="14" stroke="var(--red)"/>
    </g>
    <g class="num" text-anchor="middle"><text x="228" y="204">01</text><text x="302" y="204">02</text><text x="376" y="204">03</text><text x="448" y="204">04</text></g>
    <text class="label-sm" x="47" y="67" style="font-size:6px">TEXT TITTLE HERE</text>
    <text class="label-sm" x="47" y="156" style="font-size:6px">TEXT TITTLE HERE</text>
    <g stroke="#999" stroke-width=".8"><line x1="47" y1="80" x2="155" y2="80"/><line x1="47" y1="169" x2="155" y2="169"/><line x1="530" y1="90" x2="638" y2="90"/><line x1="530" y1="175" x2="638" y2="175"/></g>
    <g class="body-dark" style="font-size:4.8px">
      <text x="47" y="97">Lorep ipsum duis aute irure dolor in</text><text x="47" y="107">kauselh oilusioi reprehenderitlores</text><text x="47" y="117">voluptates esse</text>
      <text x="47" y="186">Lorep ipsum duis aute irure dolor in</text><text x="47" y="196">kauselh oilusioi reprehenderitlores</text><text x="47" y="206">voluptates esse</text>
    </g>
    <g text-anchor="end">
      <text class="label-sm" x="638" y="77" style="font-size:6px">TEXT TITTLE HERE</text>
      <text class="label-sm" x="638" y="162" style="font-size:6px">TEXT TITTLE HERE</text>
      <g class="body-dark" style="font-size:4.8px">
        <text x="638" y="109">Lorep ipsum duis aute irure dolor in</text><text x="638" y="119">kauselh oilusioi reprehenderitlores</text><text x="638" y="129">voluptates esse</text>
        <text x="638" y="193">Lorep ipsum duis aute irure dolor in</text><text x="638" y="203">kauselh oilusioi reprehenderitlores</text><text x="638" y="213">voluptates esse</text>
      </g>
    </g>
    <text class="footer-url" x="33" y="355">www. dalq7.ch</text>
    <text class="pager" x="588" y="349">01 /&#160;&#160;39</text><text class="pager" x="588" y="364">Welcome Slide</text>
  </svg>
</section>

<!-- Infographic: linked steps -->
<section class="slide" style="left:87px;top:713px">
  <svg viewBox="0 0 680 380">
    <text class="h2" x="73" y="93">Infographic</text>
    <path d="M150 236Q176 236 183 200" fill="none" stroke="var(--red)" stroke-width="11"/>
    <path d="M584 200Q591 236 618 236" fill="none" stroke="var(--red)" stroke-width="11"/>
    <g>
      <path d="M182 195A46 46 0 0 1 274 195Z" fill="var(--red)"/><path d="M274 195A46 46 0 0 1 182 195Z" fill="var(--grey)"/>
      <path d="M259 195A46 46 0 0 1 351 195Z" fill="var(--ink)"/><path d="M351 195A46 46 0 0 1 259 195Z" fill="var(--red)"/>
      <path d="M337 195A46 46 0 0 1 429 195Z" fill="var(--red)"/><path d="M429 195A46 46 0 0 1 337 195Z" fill="var(--grey)"/>
      <path d="M415 195A46 46 0 0 1 507 195Z" fill="var(--ink)"/><path d="M507 195A46 46 0 0 1 415 195Z" fill="var(--red)"/>
      <path d="M493 195A46 46 0 0 1 585 195Z" fill="var(--red)"/><path d="M585 195A46 46 0 0 1 493 195Z" fill="var(--grey)"/>
    </g>
    <g fill="#fff"><circle cx="228" cy="195" r="34"/><circle cx="305" cy="195" r="34"/><circle cx="383" cy="195" r="34"/><circle cx="461" cy="195" r="34"/><circle cx="539" cy="195" r="34"/></g>
    <g stroke="#fff" stroke-width="2">
      <circle cx="228" cy="195" r="28" fill="var(--ink)"/><circle cx="305" cy="195" r="28" fill="var(--red)"/>
      <circle cx="383" cy="195" r="28" fill="var(--ink)"/><circle cx="461" cy="195" r="28" fill="var(--red)"/>
      <circle cx="539" cy="195" r="28" fill="var(--ink)"/>
    </g>
    <use href="#ic-cloud" x="214" y="181" width="28" height="28" color="#fff"/>
    <use href="#ic-puzzle" x="293" y="183" width="24" height="24" color="#fff"/>
    <use href="#ic-rocket" x="371" y="183" width="24" height="24" color="#fff"/>
    <use href="#ic-shield" x="449" y="183" width="24" height="24" color="#fff"/>
    <use href="#ic-trophy" x="527" y="183" width="24" height="24" color="#fff"/>
    <g fill="var(--ink)"><circle cx="228" cy="149" r="9"/><circle cx="305" cy="149" r="9"/><circle cx="383" cy="149" r="9"/><circle cx="461" cy="149" r="9"/><circle cx="539" cy="149" r="9"/></g>
    <g class="num-sm" text-anchor="middle"><text x="228" y="151">1</text><text x="305" y="151">2</text><text x="383" y="151">3</text><text x="461" y="151">4</text><text x="539" y="151">5</text></g>
    <g class="label-sm" style="font-size:6px">
      <text x="368" y="66">TEXT TITTLE HERE</text><text x="528" y="66">TEXT TITTLE HERE</text>
      <text x="200" y="273">TEXT TITTLE HERE</text><text x="350" y="273">TEXT TITTLE HERE</text><text x="502" y="273">TEXT TITTLE HERE</text>
    </g>
    <g stroke="#999" stroke-width=".8">
      <line x1="368" y1="78" x2="476" y2="78"/><line x1="528" y1="78" x2="636" y2="78"/>
      <line x1="200" y1="285" x2="306" y2="285"/><line x1="350" y1="285" x2="456" y2="285"/><line x1="502" y1="285" x2="610" y2="285"/>
    </g>
    <g class="body-dark" style="font-size:4.8px">
      <text x="368" y="93">Lorep ipsum duis aute irure dolor in</text><text x="368" y="103">kauselh oilusioi reprehenderitlores</text><text x="368" y="113">voluptates esse</text>
      <text x="528" y="93">Lorep ipsum duis aute irure dolor in</text><text x="528" y="103">kauselh oilusioi reprehenderitlores</text><text x="528" y="113">voluptates esse</text>
      <text x="200" y="300">Lorep ipsum duis aute irure dolor in</text><text x="200" y="310">kauselh oilusioi reprehenderitlores</text><text x="200" y="320">voluptates esse</text>
      <text x="350" y="300">Lorep ipsum duis aute irure dolor in</text><text x="350" y="310">kauselh oilusioi reprehenderitlores</text><text x="350" y="320">voluptates esse</text>
      <text x="502" y="300">Lorep ipsum duis aute irure dolor in</text><text x="502" y="310">kauselh oilusioi reprehenderitlores</text><text x="502" y="320">voluptates esse</text>
    </g>
    <text class="footer-url" x="33" y="355">www. dalq7.ch</text>
    <text class="pager" x="588" y="349">01 /&#160;&#160;39</text><text class="pager" x="588" y="364">Welcome Slide</text>
  </svg>
</section>

<!-- Contact -->
<section class="slide" style="left:465px;top:713px">
  <svg viewBox="0 0 680 380">
    <defs>
      <linearGradient id="flag-photo" x1="0" y1="0" x2="0.4" y2="1">
        <stop offset="0" stop-color="#c9d2dc"/><stop offset=".35" stop-color="#c8202a"/><stop offset=".7" stop-color="#a8142a"/><stop offset="1" stop-color="#5d6e3d"/>
      </linearGradient>
    </defs>
    <text class="logo" x="602" y="42">DALQ7</text>
    <rect x="50" y="68" width="249" height="248" fill="url(#flag-photo)" role="img" aria-label="Photo of a Swiss flag waving in front of green alpine slopes"/>
    <rect x="50" y="316" width="386" height="64" fill="var(--red)"/>
    <text class="white" x="102" y="352" style="font-size:7px">www. dalq7.ch</text>
    <text class="white" x="240" y="346" style="font-size:6px;letter-spacing:.8px">LOREM IPSUM</text>
    <text x="240" y="362" style="font-size:5.5px;fill:#f5c2c5;letter-spacing:.8px">Tittle Here</text>
    <line x1="363" y1="350" x2="396" y2="350" stroke="#fff" stroke-width="1" marker-end="url(#arrow-white)"/>
    <text x="363" y="104" style="font-size:28px;font-weight:500;fill:var(--ink)">Contact</text>
    <g class="body" style="font-size:4.6px">
      <text x="368" y="131">Lorem ipsum dolor siabes dolore magna aliqua utaners enim vas adtera inte</text>
      <text x="368" y="141">minimes veniamo contetur adipiscing elita essieund do eiusmod tempor</text>
      <text x="368" y="151">indidunt auteran laborevet ullamco lasiedo nisi aliquie com modo conse.</text>
    </g>
    <g class="label-sm" style="font-size:6.5px;letter-spacing:1.2px;fill:var(--char)">
      <text x="368" y="192">OFFICE HOURS</text><text x="524" y="192">OUR ADDRESS</text>
      <text x="370" y="258">FOLLOW US</text><text x="522" y="258">GET IN TOUCH</text>
    </g>
    <g class="body" style="font-size:4.6px">
      <text x="368" y="206">Monday – Friday</text><text x="368" y="216">09:00 – 16.00</text>
      <text x="526" y="205">00, Street Name,</text><text x="526" y="215">City 0000</text>
      <text x="370" y="271">www.yourwebsite.com</text><text x="370" y="281">name@yourmail.com</text>
      <text x="523" y="271">(+00) 000 000 0000</text><text x="523" y="281">(+00) 000 000 0001</text>
    </g>
    <text class="pager" x="588" y="349">01 /&#160;&#160;39</text><text class="pager" x="588" y="364">Welcome Slide</text>
  </svg>
</section>

<!-- Thank You -->
<section class="slide" style="left:87px;top:928px">
  <svg viewBox="0 0 680 380">
    <defs>
      <linearGradient id="mountain-photo" x1="0" y1="0" x2="0" y2="1">
        <stop offset="0" stop-color="#a7aca9"/><stop offset=".35" stop-color="#6e716d"/><stop offset=".7" stop-color="#3b3d3a"/><stop offset="1" stop-color="#1d201d"/>
      </linearGradient>
    </defs>
    <rect width="680" height="380" fill="url(#mountain-photo)" role="img" aria-label="Photo of rugged alpine peaks with clouds and dark pine forest"/>
    <text x="320" y="122" text-anchor="middle" style="font-size:42px;font-weight:600;fill:#fff;letter-spacing:2px">DALQ7</text>
    <text x="66" y="236" style="font-size:98px;font-weight:600;fill:#fff;letter-spacing:-1px">Thank You</text>
    <g fill="none" stroke="#fff" stroke-width="1"><circle cx="325" cy="298" r="4.5"/><circle cx="371" cy="298" r="4.5"/></g>
    <circle cx="348" cy="298" r="5" fill="var(--red)"/>
    <text x="33" y="359" style="font-size:7.5px;fill:#fff">www. dalq7.ch</text>
    <text x="506" y="364" style="font-size:8px;fill:#fff">TRUST</text>
    <line x1="548" y1="361" x2="601" y2="361" stroke="#fff" stroke-width="1"/>
    <text x="609" y="364" style="font-size:8px;fill:#fff">ECONOMY</text>
  </svg>
</section>

</body>
</html>
```